Vale Crest Motors Business Card

Would like a cutting edge / high end Automotive Business card design. Please see current card which is old and dated. Would like to maintain the Vale Crest Motors logo and same information (address, website, etc).

See our website for the look and feel of what we offer - www.valecrestmotors.example

Target Market(s)

Upper class car buyers

Contact Information for Business Card

Modern high end business card design

Requirements
Nice to have
• Carbon Fiber look background

```html
<!DOCTYPE html>
<html lang="en">
<head>
<meta charset="utf-8">
<title>Vale Crest Motors Business Card</title>
<link href="https://fonts.googleapis.com/css2?family=Jura:wght@500;600&display=swap" rel="stylesheet">
<style>
  :root {
    --backdrop: #c4983c;
    --card-black: #0b0b0b;
    --card-grey: #1c1c1c;
    --gold: #e2bb5a;
    --white: #ffffff;
    --ink: #141414;
    --ember: rgba(150, 40, 20, 0.45);
    --amber: rgba(140, 90, 30, 0.35);
  }
  * { margin: 0; padding: 0; box-sizing: border-box; }
  html, body { width: 1200px; height: 1067px; overflow: hidden; }
  body {
    background: var(--backdrop);
    position: relative;
    font-family: "Jura", sans-serif;
    font-weight: 500;
    color: var(--white);
  }
  .card {
    position: absolute;
    top: 95px;
    width: 505px;
    height: 884px;
    background:
      radial-gradient(circle at 0% 100%, var(--ember), transparent 28%),
      radial-gradient(circle at 100% 0%, var(--amber), transparent 25%),
      radial-gradient(circle at 100% 50%, rgba(255,255,255,0.06), transparent 40%),
      linear-gradient(160deg, var(--card-grey), var(--card-black) 55%, var(--card-grey));
    overflow: hidden;
  }
  .card--front { left: 78px; }
  .card--back { left: 613px; }

  .brand-name {
    position: absolute;
    left: 0; right: 0;
    text-align: center;
    font-weight: 600;
    color: var(--white);
    text-transform: uppercase;
    line-height: 1.05;
    letter-spacing: 2px;
  }
  .card--front .brand-name { top: 92px; font-size: 50px; }
  .card--back .brand-name { top: 178px; font-size: 40px; }

  .holder-name {
    position: absolute;
    right: 40px;
    top: 280px;
    font-size: 50px;
    color: var(--gold);
    letter-spacing: 3px;
  }
  .holder-role {
    position: absolute;
    right: 40px;
    top: 334px;
    font-size: 23px;
    letter-spacing: 1.5px;
  }

  .contact-label {
    position: absolute;
    left: 54px;
    height: 23px;
    padding: 0 8px;
    background: var(--gold);
    color: var(--ink);
    font-size: 20px;
    font-weight: 600;
    line-height: 23px;
    letter-spacing: 1px;
  }
  .contact-value {
    position: absolute;
    left: 54px;
    font-size: 22px;
    line-height: 29px;
    letter-spacing: 1px;
    white-space: nowrap;
  }

  .tagline {
    position: absolute;
    left: 0; right: 0;
    top: 682px;
    text-align: center;
    font-size: 19px;
    line-height: 24px;
    letter-spacing: 1.5px;
  }
  .values-badge {
    position: absolute;
    left: 143px;
    top: 748px;
    width: 219px;
    height: 19px;
    background: var(--gold);
    color: var(--ink);
    font-size: 14px;
    font-weight: 600;
    line-height: 19px;
    text-align: center;
    letter-spacing: 0.8px;
  }
</style>
</head>
<body>
  <section class="card card--front" role="img" aria-label="Business card front on a dark carbon fibre weave background">
    <div class="brand-name">Vale Crest<br>Motors</div>
    <div class="holder-name">Daniel Marsh</div>
    <div class="holder-role">Owner</div>

    <div class="contact-label" style="top:445px">ADDRESS</div>
    <div class="contact-value" style="top:470px">1480 Harbor Ridge Rd #B<br>Linden, CA 94000</div>

    <div class="contact-label" style="top:552px">PHONE</div>
    <div class="contact-value" style="top:577px">555 201 4830</div>

    <div class="contact-label" style="top:619px">FAX</div>
    <div class="contact-value" style="top:645px">555 201 4831</div>

    <div class="contact-label" style="top:692px">EMAIL</div>
    <div class="contact-value" style="top:717px">daniel@valecrestmotors.example</div>

    <div class="contact-label" style="top:766px">WEBSITE</div>
    <div class="contact-value" style="top:793px">www.valecrestmotors.example</div>
  </section>

  <section class="card card--back" role="img" aria-label="Business card back on a dark carbon fibre weave background">
    <div class="brand-name">Vale Crest<br>Motors</div>
    <div class="tagline">Offering the Finest in<br>Luxury &amp; Exotic Sport Cars</div>
    <div class="values-badge">Quality | Integrity | Service</div>
  </section>
</body>
</html>
```